Business Card for Managing Partner Investment Fund

To create a business card template for an investment fund manager. Business card should be more professional in nature, not too colorful, more upscale, and created using the attached logos and fund name files. I would prefer a black or gray color scheme, but am open to the use of color as well. I would prefer a double sided business card, but open to single sided business card designs as well. The business card should include: name, title, and contact information, as well as logo and company name. I would prefer a more stream-lined, simple business card design.
Updates
Address: 4190 NE 38th Ter. Ocala, FL 34470
Email: talvin47@quorimail.net
Phone: 561-347-9162
Title: managing partner
Name: Dorian Velsky
Fund Name: Ambergate Capital
Logos can be found in files attached to the brief
Target Market(s)
potential investors, other fund managers
Industry/Entity Type
Finance
Contact Information for Business Card
Name on card: Dorian Velsky
Title: Managing Partner
Colors
Designer to choose colors to be used in the design.
Requirements
Must have
- Phone number
- email address
- physical address
- title
- name
- logo
- Fund name
Nice to have
- simple layout
Should not have
- too many colors, busy fonts,

```html
<!DOCTYPE html>
<html lang="en">
<head>
<meta charset="utf-8">
<title>Ambergate Capital — Business Card</title>
<link rel="stylesheet" href="https://fonts.googleapis.com/css2?family=Cinzel:wght@600&family=Oswald:wght@600&family=Poppins:wght@400;500&display=swap">
<style>
  :root {
    --stage: #1b1a1a;
    --card-light: #ffffff;
    --card-dark: #2b2827;
    --ink: #1e1c1c;
    --ink-soft: #3a3838;
    --paper-text: #ffffff;
    --rule: #1e1c1c;
  }
  * { margin: 0; padding: 0; box-sizing: border-box; }
  html, body {
    width: 1200px; height: 1000px; overflow: hidden;
    background: var(--stage);
  }
  .canvas {
    position: relative; width: 1200px; height: 1000px;
    display: flex; flex-direction: column; align-items: center; justify-content: center;
    gap: 64px;
  }
  .card {
    position: relative; width: 600px; height: 343px;
    border-radius: 16px; overflow: hidden;
    box-shadow: 0 10px 30px rgba(0,0,0,.5);
  }

  /* Front */
  .card--front { background: var(--card-light); color: var(--ink); }
  .brand-name {
    font-family: "Cinzel", serif; font-weight: 600;
    display: flex; align-items: center; gap: 12px; letter-spacing: 2px;
  }
  .brand-name__mark { width: 14px; height: 14px; background: currentColor; }
  .card--front .brand-name {
    position: absolute; left: 40px; top: 44px; font-size: 26px; color: var(--ink);
  }
  .divider {
    position: absolute; left: 40px; top: 150px; width: 300px; height: 2px;
    background: var(--rule);
  }
  .contact-list {
    position: absolute; left: 40px; top: 178px; list-style: none;
    font-family: "Poppins", sans-serif; font-size: 13px; color: var(--ink-soft);
  }
  .contact-list li { display: flex; align-items: center; gap: 10px; height: 26px; }
  .contact-list svg { width: 13px; height: 13px; fill: var(--ink); }
  .holder {
    position: absolute; left: 356px; top: 134px;
  }
  .holder__name {
    font-family: "Oswald", sans-serif; font-weight: 600; font-size: 24px;
    letter-spacing: 1px; text-transform: uppercase; line-height: 1.1;
  }
  .holder__title {
    font-family: "Poppins", sans-serif; font-weight: 500; font-size: 12px;
    letter-spacing: 1px; text-transform: uppercase; margin-top: 2px;
  }
  .holder__address {
    font-family: "Poppins", sans-serif; font-size: 13px; color: var(--ink-soft);
    margin-top: 18px; line-height: 1.6; font-style: normal;
  }
  .footer-band { position: absolute; left: 0; bottom: 0; width: 600px; height: 44px; }
  .footer-band__label {
    position: absolute; right: 34px; bottom: 11px;
    font-family: "Cinzel", serif; font-weight: 600; font-size: 11px;
    letter-spacing: 1px; color: var(--paper-text);
  }

  /* Back */
  .card--back {
    background: var(--card-dark);
    display: flex; align-items: center; justify-content: center;
  }
  .card--back .brand-name { font-size: 40px; color: var(--paper-text); gap: 18px; }
  .card--back .brand-name__mark { width: 20px; height: 20px; }
</style>
</head>
<body>
<main class="canvas">

  <section class="card card--front" aria-label="Card front">
    <div class="brand-name"><span class="brand-name__mark"></span>Ambergate Capital</div>
    <div class="divider"></div>

    <ul class="contact-list">
      <li>
        <svg viewBox="0 0 24 24" aria-hidden="true"><path d="M6.6 10.8a15.1 15.1 0 0 0 6.6 6.6l2.2-2.2a1 1 0 0 1 1-.25 11.4 11.4 0 0 0 3.6.57 1 1 0 0 1 1 1V20a1 1 0 0 1-1 1A17 17 0 0 1 3 4a1 1 0 0 1 1-1h3.5a1 1 0 0 1 1 1c0 1.25.2 2.45.57 3.57a1 1 0 0 1-.25 1z"/></svg>
        561-347-9162
      </li>
      <li>
        <svg viewBox="0 0 24 24" aria-hidden="true"><path d="M2 5h20v14H2zm2 2v.5l8 5 8-5V7l-8 5z"/></svg>
        talvin47@quorimail.net
      </li>
    </ul>

    <div class="holder">
      <div class="holder__name">Dorian Velsky</div>
      <div class="holder__title">Managing Partner</div>
      <address class="holder__address">4190 NE 38th Ter.<br>Ocala, FL 34470</address>
    </div>

    <svg class="footer-band" viewBox="0 0 600 44" aria-hidden="true">
      <path d="M0 30 H318 L336 14 H600 V44 H0 Z" fill="var(--ink)"/>
      <path d="M0 30 H318 L336 14 H600 V18 H338 L320 34 H0 Z" fill="var(--ink-soft)"/>
    </svg>
    <div class="footer-band__label">AMBERGATE CAPITAL</div>
  </section>

  <section class="card card--back" aria-label="Card back">
    <div class="brand-name"><span class="brand-name__mark"></span>Ambergate Capital</div>
  </section>

</main>
</body>
</html>
```